Morvela Aesthetic Doctor

I require an elegant, luxurious looking business card for my aesthetic business. I am a doctor and that will set me aside from competitors. I am planning to provide home and spa based treatments to clients with high expectations. I have attached my logo.

```html
<!DOCTYPE html>
<html lang="en">
<head>
<meta charset="UTF-8">
<title>Morvela Aesthetic Doctor – Business Card</title>
<link rel="stylesheet" href="https://fonts.googleapis.com/css2?family=Cinzel:wght@400&family=Arimo:wght@400;700&display=swap">
<style>
  :root{
    --bg:#e9ebee;
    --blue:#2a9fd8;
    --blue-deep:#1b86c4;
    --blue-dark:#1779b8;
    --sky:#3aa6e0;
    --grey:#8e9194;
    --grey-light:#b3b5b8;
    --ink:#4a4d50;
    --white:#ffffff;
  }
  *{margin:0;padding:0;box-sizing:border-box}
  html,body{width:1200px;height:901px;overflow:hidden;background:var(--bg)}
  .canvas{position:relative;width:1200px;height:901px}
  .card{position:absolute;left:250px;width:700px;height:400px;overflow:hidden;box-shadow:0 6px 18px rgba(0,0,0,.18)}
  /* front */
  .card--front{top:30px;background:radial-gradient(ellipse at 50% 40%,#35b0e6 0%,var(--blue) 55%,var(--blue-deep) 100%)}
  .front__mark{position:absolute;left:260px;top:75px;width:180px;height:180px;border:3px solid var(--white);border-radius:50%;display:flex;align-items:center;justify-content:center}
  .front__name{font-family:'Arimo',sans-serif;font-weight:400;font-size:26px;color:var(--white);letter-spacing:1px}
  .front__tagline{position:absolute;left:0;right:0;top:322px;text-align:center;font-family:'Arimo',sans-serif;font-size:16px;color:var(--white)}
  /* back */
  .card--back{top:470px;background:var(--white)}
  .wordmark{position:absolute;left:42px;top:58px;line-height:1}
  .wordmark__name{display:block;font-family:'Cinzel',serif;font-size:74px;color:var(--grey);letter-spacing:2px}
  .wordmark__sub{display:block;font-family:'Cinzel',serif;font-size:33px;color:var(--sky);letter-spacing:1px;margin-top:-4px}
  .doctor{position:absolute;left:46px;top:178px;font-family:'Arimo',sans-serif}
  .doctor__name{font-weight:700;font-size:28px;color:var(--blue-dark)}
  .doctor__post{font-size:14px;color:var(--ink);margin-left:4px}
  .doctor__cred{font-size:14px;color:var(--ink);margin-top:2px}
  .rule{position:absolute;height:2px;background:var(--blue-deep)}
  .rule--one{left:46px;top:236px;width:340px}
  .rule--two{left:46px;top:328px;width:440px}
  .contact{position:absolute;left:46px;top:246px;list-style:none;font-family:'Arimo',sans-serif;font-size:15px;color:var(--ink)}
  .contact li{display:flex;align-items:center;height:25px}
  .contact svg{width:16px;height:16px;margin-right:10px;flex:none}
  .services{position:absolute;left:46px;top:336px;font-family:'Arimo',sans-serif;font-size:15px;color:var(--ink);line-height:21px}
  .band{position:absolute;left:0;top:0}
  .band__tagline{position:absolute;right:40px;top:342px;font-family:'Arimo',sans-serif;font-size:15px;color:var(--white)}
  .back__mark{position:absolute;left:440px;top:40px;width:230px;height:230px;border:4px solid var(--grey-light);border-radius:50%;display:flex;align-items:center;justify-content:center}
  .back__name{font-family:'Arimo',sans-serif;font-weight:400;font-size:30px;color:var(--sky);letter-spacing:1px}
</style>
</head>
<body>
<main class="canvas">
  <section class="card card--front" aria-label="Card front">
    <div class="front__mark"><span class="front__name">Morvela</span></div>
    <p class="front__tagline">Home and Spa Based Treatments</p>
  </section>

  <section class="card card--back" aria-label="Card back">
    <svg class="band" width="700" height="400" viewBox="0 0 700 400" aria-hidden="true">
      <path d="M0 386 L380 386 L380 372 Q384 330 430 330 L700 330 L700 400 L0 400 Z" fill="var(--blue)"/>
      <path d="M0 380 L370 380 L372 370" stroke="var(--grey-light)" stroke-width="2" fill="none"/>
    </svg>

    <h1 class="wordmark">
      <span class="wordmark__name">MORVELA</span>
      <span class="wordmark__sub">AESTHETIC DOCTOR</span>
    </h1>

    <div class="doctor">
      <p><span class="doctor__name">Dr Elise Marten</span><span class="doctor__post">MRCPCH MD</span></p>
      <p class="doctor__cred">Australasian Diploma of Aesthetic Medicine</p>
    </div>
    <div class="rule rule--one"></div>

    <ul class="contact">
      <li><svg viewBox="0 0 16 16"><path d="M3 1.5l3 3-1.5 2a9 9 0 0 0 5 5l2-1.5 3 3-2 2C7 14.5 1.5 9 1 3z" fill="var(--blue-dark)"/></svg>0800 555 014</li>
      <li><svg viewBox="0 0 16 16"><rect x="1" y="3" width="14" height="10" fill="none" stroke="var(--blue-dark)" stroke-width="1.3"/><path d="M1 3l7 6 7-6" fill="none" stroke="var(--blue-dark)" stroke-width="1.3"/></svg>elise@morvela.co.nz</li>
      <li><svg viewBox="0 0 16 16"><circle cx="8" cy="8" r="6.5" fill="none" stroke="var(--blue-dark)" stroke-width="1.3"/><ellipse cx="8" cy="8" rx="3" ry="6.5" fill="none" stroke="var(--blue-dark)" stroke-width="1.1"/><path d="M1.5 8h13M2.5 5h11M2.5 11h11" stroke="var(--blue-dark)" stroke-width="1"/></svg>www.morvela.co.nz</li>
    </ul>
    <div class="rule rule--two"></div>

    <p class="services">Dermal injectables - Plasma facials - Microneedling<br>Skin boosters - Excessive sweating</p>

    <p class="band__tagline">Home and Spa Based Treatments</p>

    <div class="back__mark"><span class="back__name">Morvela</span></div>
  </section>
</main>
</body>
</html>
```